Hello again

I have a few Logos I am looking to add

Target Market(s)

MediSpa

Industry/Entity Type

Medispa

Contact Information for Business Card

Dana Whitcombe, Owner/Medical Aesthetician, 403-812-3957, Unit 148 - 1920 5 st NW, T3K 1M7 Calgary, AB., www.LarkMediSpa.ca ....QR codes are attached I do really like the former business card but everything was in teal, gold and white.

```html
<!DOCTYPE html>
<html lang="en">
<head>
<meta charset="utf-8">
<title>Lark MediSpa – Business Card</title>
<link href="https://fonts.googleapis.com/css2?family=Marcellus&family=Jost:wght@400;500&display=swap" rel="stylesheet">
<style>
  :root {
    --backdrop: #1b1b1b;
    --ink: #0f0f0f;
    --paper: #ece9e4;
    --gold: #b88f4f;
    --gold-light: #d6b375;
    --white: #f4f1ec;
    --text-dark: #1a1a1a;
  }
  * { box-sizing: border-box; margin: 0; padding: 0; }
  html, body {
    width: 1200px; height: 1006px; overflow: hidden;
    background: var(--backdrop);
  }
  .canvas { position: relative; width: 1200px; height: 1006px; }

  .card { position: absolute; left: 190px; width: 820px; overflow: hidden; }

  /* Front */
  .card-front { top: 60px; height: 452px; background: var(--ink); }
  .card-front .frame {
    position: absolute; inset: 14px;
    border: 1px solid var(--gold);
  }
  .front-brand {
    position: absolute; left: 0; right: 0; top: 170px;
    text-align: center;
  }
  .brand-name {
    font-family: "Marcellus", serif;
    color: var(--gold-light);
    font-weight: 400;
    letter-spacing: 0.06em;
    white-space: nowrap;
  }
  .front-brand .brand-name { font-size: 84px; line-height: 1; }
  .brand-tagline {
    font-family: "Jost", sans-serif;
    font-weight: 500;
    color: var(--gold);
    letter-spacing: 0.28em;
    white-space: nowrap;
  }
  .front-brand .brand-tagline { font-size: 16px; margin-top: 20px; }

  /* Back */
  .card-back { top: 540px; height: 428px; background: var(--paper); }
  .card-back .dark-wave { position: absolute; inset: 0; }
  .holder { position: absolute; left: 66px; top: 80px; width: 380px; }
  .holder-name {
    font-family: "Marcellus", serif;
    font-size: 38px;
    letter-spacing: 0.16em;
    color: var(--text-dark);
    white-space: nowrap;
  }
  .holder-title {
    font-family: "Jost", sans-serif;
    font-weight: 500;
    font-size: 17px;
    letter-spacing: 0.14em;
    color: var(--gold);
    margin-top: 6px;
    white-space: nowrap;
  }
  .divider {
    display: flex; align-items: center; gap: 12px;
    margin-top: 24px; width: 360px;
  }
  .divider .rule { flex: 1; height: 1px; background: var(--gold); opacity: 0.6; }
  .divider .dot { width: 7px; height: 7px; border-radius: 50%; background: var(--gold); }

  .contact-list { position: absolute; left: 64px; top: 212px; list-style: none; }
  .contact-item {
    display: flex; align-items: center; gap: 22px;
    font-family: "Jost", sans-serif; font-size: 19px;
    color: var(--text-dark); line-height: 1.3;
  }
  .contact-item + .contact-item { margin-top: 22px; }
  .contact-icon {
    width: 38px; height: 38px; flex: none;
    border: 1.5px solid var(--gold); border-radius: 50%;
    display: flex; align-items: center; justify-content: center;
  }
  .contact-icon svg { width: 20px; height: 20px; }

  .back-brand { position: absolute; left: 525px; top: 318px; width: 260px; text-align: center; }
  .back-brand .brand-name { font-size: 32px; line-height: 1; }
  .back-brand .brand-tagline { font-size: 8.5px; margin-top: 9px; letter-spacing: 0.22em; }
</style>
</head>
<body>
<main class="canvas">

  <section class="card card-front" aria-label="Card front">
    <div class="frame"></div>
    <div class="front-brand">
      <div class="brand-name">LARK MEDISPA</div>
      <div class="brand-tagline">SKIN &amp; LASER SPECIALISTS</div>
    </div>
  </section>

  <section class="card card-back" aria-label="Card back">
    <svg class="dark-wave" viewBox="0 0 820 428" preserveAspectRatio="none" aria-hidden="true">
      <path d="M712 0 C 694 120, 600 170, 560 250 C 520 330, 495 380, 482 428 H820 V0 Z" fill="#0f0f0f"/>
      <path d="M712 0 C 694 120, 600 170, 560 250 C 520 330, 495 380, 482 428" fill="none" stroke="#c9a262" stroke-width="5"/>
    </svg>

    <div class="holder">
      <h1 class="holder-name">DANA WHITCOMBE</h1>
      <p class="holder-title">OWNER / MEDICAL AESTHETICIAN</p>
      <div class="divider"><span class="rule"></span><span class="dot"></span><span class="rule"></span></div>
    </div>

    <ul class="contact-list">
      <li class="contact-item">
        <span class="contact-icon">
          <svg viewBox="0 0 24 24"><path d="M6.6 3.5l2.6 3.2c.4.5.3 1.1-.1 1.5L7.7 9.6c1 2.3 2.7 4 5 5l1.4-1.4c.4-.4 1-.5 1.5-.1l3.2 2.6c.5.4.5 1.1.1 1.6l-1.6 1.8c-.5.5-1.2.7-1.9.5C9.4 18.2 5.8 14.6 4.4 8.6c-.2-.7 0-1.4.5-1.9L6.6 5c.1-.6 0-1.5 0-1.5z" fill="#b88f4f"/></svg>
        </span>
        <span>403-812-3957</span>
      </li>
      <li class="contact-item">
        <span class="contact-icon">
          <svg viewBox="0 0 24 24"><path d="M12 2.5c-3.6 0-6.3 2.8-6.3 6.3 0 4.6 6.3 12.7 6.3 12.7s6.3-8.1 6.3-12.7c0-3.5-2.7-6.3-6.3-6.3zm0 8.8a2.5 2.5 0 1 1 0-5 2.5 2.5 0 0 1 0 5z" fill="#b88f4f"/></svg>
        </span>
        <span>Unit 148 - 1920 5 st NW,<br>T3K 1M7 Calgary, AB.</span>
      </li>
      <li class="contact-item">
        <span class="contact-icon">
          <svg viewBox="0 0 24 24" fill="none" stroke="#b88f4f" stroke-width="1.5"><circle cx="12" cy="12" r="9"/><ellipse cx="12" cy="12" rx="4" ry="9"/><path d="M3 12h18M4.5 7.5h15M4.5 16.5h15"/></svg>
        </span>
        <span>www.LarkMediSpa.ca</span>
      </li>
    </ul>

    <div class="back-brand">
      <div class="brand-name">LARK MEDISPA</div>
      <div class="brand-tagline">SKIN &amp; LASER SPECIALISTS</div>
    </div>
  </section>

</main>
</body>
</html>
```